CONTACT US Page and design for website

We need a contact us page for our website. We would like it to have a message area, a map, our information, etc.

Please see the text attachment for what we are looking for. We need to have something that is creative and interesting, modern and professional.

We believe that a contact US page should be very creative because everyone clicks that to contact us. We want it to be super professional, attention grabbing, pleasing to the eye.

PLEASE KEEP THE HEADER AND FOOTER THE SAME, ONLY THE ACTUAL CONTACT US PAGE NEEDS TO BE WORKED ON. THANKS!
We are excited to work with designers for this project.

Target Market(s)

Clients in technology business

Industry/Entity Type

Information Technology

Number of Pages Required

1 page

Font styles to use
Serif

Requirements
Must have
• CHECK THE TEXT ATTACHMENT PLEASE
• Must stay within our design colors and theme.
Nice to have
• see attachment
Should not have
• it should be special

```html
<!DOCTYPE html>
<html lang="en">
<head>
<meta charset="utf-8">
<title>Contact Us – Nexora Tech</title>
<link href="https://fonts.googleapis.com/css2?family=Roboto:wght@400;500;700&family=Roboto+Condensed:wght@400;700&display=swap" rel="stylesheet">
<style>
:root{
  --teal:#2ccdb8;
  --teal-dark:#1fa898;
  --ink:#222;
  --dark:#1d1f20;
  --map:#3a3a3a;
  --grey:#a9a9a9;
  --grey-dark:#8f8f8f;
  --white:#fff;
}
*{margin:0;padding:0;box-sizing:border-box}
html,body{width:1198px;height:1200px;overflow:hidden;background:var(--white);font-family:"Roboto",Arial,sans-serif;color:var(--ink)}
.page{position:relative;width:1198px;height:1200px}
.abs{position:absolute}

/* header */
.header{top:0;left:0;width:1198px;height:68px;border-top:2px solid var(--teal-dark);border-bottom:1px solid #ddd}
.brand{left:56px;top:18px;font:700 30px "Roboto Condensed",sans-serif;color:var(--teal);letter-spacing:3px;display:flex;align-items:center;gap:10px}
.brand i{width:20px;height:20px;background:var(--teal);border-radius:50%;display:block}
.account{right:44px;top:0;width:130px;height:24px;background:#8a8a8a;border-radius:0 0 18px 18px;display:flex;font-size:8px;color:#fff}
.account span{flex:1;display:flex;align-items:center;justify-content:center}
.account span:first-child{background:#b0b0b0;border-radius:0 0 0 18px;color:#333}
.contact-top{right:43px;top:33px;display:flex;align-items:center;gap:10px;font-size:10px}
.circle{width:26px;height:26px;border:1px solid #ccc;border-radius:50%;display:flex;align-items:center;justify-content:center}
.contact-top .phone{font-size:13px}
.nav{top:68px;left:0;width:1198px;height:34px;border-bottom:1px solid #ddd}
.nav ul{position:absolute;left:61px;top:12px;display:flex;gap:18px;list-style:none;font-size:9.5px;color:#333}
.search{right:99px;top:8px;width:165px;height:20px;border:1px solid #ccc;border-radius:10px;font-size:8px;padding:5px 14px;color:#333}
.cart{right:58px;top:6px}
.crumb{top:102px;left:0;width:1198px;height:26px;background:var(--teal);font:700 9px "Roboto",sans-serif;color:#fff;padding:9px 121px}
.crumb b{color:#2a4a46}

/* map */
.map{top:128px;left:0;width:1198px;height:312px;background:linear-gradient(180deg,#3d3d3d,#333)}

/* contact */
.contact{top:440px;left:0;width:1198px;height:390px;background:radial-gradient(circle at 90% 80%,#1a3a38 0,var(--dark) 40%),var(--dark);border-top:2px solid var(--teal)}
.contact-mark{left:539px;top:380px;width:120px;height:120px;background:#1d1f20;border:2px solid var(--teal);border-radius:50%;display:flex;align-items:center;justify-content:center;font:700 16px "Roboto Condensed",sans-serif;color:var(--teal);letter-spacing:1px}
.field{background:#fff;border:2px solid #8ef0e2;box-shadow:0 0 8px var(--teal);font-size:10.5px;color:#888;padding:9px 12px}
.submit{left:281px;top:727px;width:87px;height:30px;background:var(--teal);color:#fff;font-size:13px;display:flex;align-items:center;justify-content:center}
.hours{left:669px;top:508px;color:#fff;font:700 13px "Roboto Condensed",sans-serif}
.hours h2{color:var(--teal);font-size:18px;margin-bottom:18px}
.hours p{margin-bottom:13px}
.hours p b{color:var(--teal);font-size:17.5px}
.inquiries{left:937px;top:496px;color:#fff;font:700 13px "Roboto Condensed",sans-serif;line-height:24px}
.inquiries a{color:var(--teal);text-decoration:none}
.inquiries div{margin-bottom:23px}
.wordmark{left:0;width:1198px;top:768px;text-align:center;font:700 40px "Roboto Condensed",sans-serif;color:var(--teal);letter-spacing:5px}

/* service band */
.band{top:832px;left:0;width:1198px;height:30px;border-top:2px solid var(--teal);border-bottom:2px solid var(--teal);text-align:center;font:700 13px "Roboto Condensed",sans-serif;color:#444;padding-top:5px}

/* footer */
.footer{top:866px;left:0;width:1198px;height:219px;background:var(--grey);color:#fff}
.about{left:320px;top:28px;width:558px;text-align:center;font:500 9.5px/13px "Roboto",sans-serif}
.facts{left:360px;top:90px;display:flex;gap:40px;font-size:10px;border-top:1px solid #bbb;padding-top:6px;width:560px}
.facts span{display:flex;gap:6px}
.links{left:315px;top:138px;display:flex;gap:0;font:500 11.5px "Roboto",sans-serif}
.links div{margin-right:60px}
.links small{display:block;font-size:6.5px;text-align:center;line-height:9.5px;margin-top:4px}
.bottom{top:1085px;left:0;width:1198px;height:115px;background:var(--grey-dark)}
.social{left:532px;top:15px;display:flex;gap:10px}
.social span{width:26px;height:26px;border:1px solid #ccc;border-radius:50%}
.rule{left:160px;top:51px;width:878px;height:1px;background:#aaa}
.legal{left:0;width:1198px;top:63px;text-align:center;color:#fff;font:700 9px/12px "Roboto",sans-serif}
.chat{right:11px;bottom:0;width:142px;height:18px;background:var(--teal);color:#fff;font:700 9px "Roboto",sans-serif;padding:4px 6px}
</style>
</head>
<body>
<div class="page">
  <header class="header abs">
    <div class="brand abs"><i></i>NEXORA TECH</div>
    <div class="account abs"><span>SIGN UP</span><span>LOGIN</span></div>
    <div class="contact-top abs">
      <span class="circle"><svg width="12" height="10" viewBox="0 0 12 10"><ellipse cx="6" cy="4.5" rx="5.5" ry="4" fill="#2ccdb8"/></svg></span>
      <span>LIVE CHAT</span>
      <span class="circle"><svg width="11" height="11" viewBox="0 0 24 24"><path d="M6.6 10.8a15 15 0 006.6 6.6l2.2-2.2a1 1 0 011-.2 11 11 0 003.6.6 1 1 0 011 1V20a1 1 0 01-1 1A17 17 0 013 4a1 1 0 011-1h3.5a1 1 0 011 1 11 11 0 00.6 3.6 1 1 0 01-.2 1z" fill="#2ccdb8"/></svg></span>
      <span class="phone">555-010-2040</span>
    </div>
  </header>
  <nav class="nav abs">
    <ul><li>SERVERS</li><li>WORKSTATIONS</li><li>COMPONENTS</li><li>VIRTUAL REALITY</li><li>DRONES</li><li>ABOUT US</li><li>BLOG</li><li>RESOURCES</li><li>CONTACT US</li></ul>
    <div class="search abs">Search</div>
    <span class="cart circle abs"><svg width="11" height="10" viewBox="0 0 11 10"><path d="M1 3h9l-1 6H2z" fill="none" stroke="#2ccdb8" stroke-width="1.4"/></svg></span>
  </nav>
  <div class="crumb abs">HOME / <b>TESTFORM</b></div>

  <div class="map abs" role="img" aria-label="Dark-styled street map showing the office location"></div>

  <section class="contact abs"></section>
  <div class="contact-mark abs">NEXORA</div>

  <div class="field abs" style="left:133px;top:498px;width:192px;height:32px">NAME</div>
  <div class="field abs" style="left:335px;top:498px;width:193px;height:32px">PHONE NUMBER</div>
  <div class="field abs" style="left:133px;top:540px;width:395px;height:32px">E-MAIL</div>
  <div class="field abs" style="left:133px;top:583px;width:395px;height:131px"></div>
  <div class="submit abs">SUBMIT</div>

  <div class="hours abs">
    <h2>HOURS OF OPERATION</h2>
    <p><b>Monday:</b> 8:00am- 5:00pm</p>
    <p><b>Tuesday:</b> 8:00am- 5:00pm</p>
    <p><b>Wednesday:</b> 8:00am- 5:00pm</p>
    <p><b>Thursday:</b> 8:00am- 5:00pm</p>
    <p><b>Friday:</b> 8:00am- 5:00pm</p>
  </div>

  <div class="inquiries abs">
    <div>General Inquiries<br>(555)010-2040<br><a>info@nexoratech.com</a></div>
    <div>Sales Inquiries<br>(555)010-2040<br><a>sales@nexoratech.com</a></div>
    <div>Purchasing Inquiries<br>(555)010-2041<br><a>purchasing@nexoratech.com</a></div>
  </div>

  <div class="wordmark abs">NEXORA TECH</div>

  <div class="band abs">OUR DEDICATED CUSTOMER SERVICE REPRESENTATIVES ARE AVAILABLE 24/7 BY PHONE</div>

  <footer class="footer abs">
    <p class="about abs">Based in Westfield Park California, Nexora Tech offers custom servers, storage, and workstations for local businesses in Los Angeles, Beverly Hills, Thousand Oaks, Ventura, Orange County, Santa Barbara, Oxnard, Irvine, Anaheim, and San Diego. Nexora Tech also offers such products to clients throughout the United States and Worldwide.</p>
    <div class="facts abs">
      <span><svg width="8" height="10" viewBox="0 0 8 10"><path d="M4 10S0 5.5 0 4a4 4 0 018 0c0 1.5-4 6-4 6z" fill="#fff"/></svg>4820 Orrin Ave.<br>Westfield Park, CA 90000</span>
      <span><svg width="9" height="9" viewBox="0 0 24 24"><path d="M6.6 10.8a15 15 0 006.6 6.6l2.2-2.2a1 1 0 011-.2 11 11 0 003.6.6 1 1 0 011 1V20a1 1 0 01-1 1A17 17 0 013 4a1 1 0 011-1h3.5a1 1 0 011 1 11 11 0 00.6 3.6 1 1 0 01-.2 1z" fill="#fff"/></svg>555-010-2040</span>
      <span><svg width="10" height="8" viewBox="0 0 10 8"><rect width="10" height="8" fill="#fff"/><path d="M0 0l5 4 5-4" stroke="#a9a9a9" fill="none"/></svg>sales@nexoratech.com</span>
    </div>
    <div class="links abs">
      <div>Computer Hardware</div><div>Drones</div><div>Virtual Reality</div><div>About Us</div>
      <div>Customer Support<small>Terms and Conditions<br>Warranty Information<br>Contact Us<br>Return Policy</small></div>
    </div>
  </footer>
  <div class="bottom abs">
    <div class="social abs"><span></span><span></span><span></span><span></span></div>
    <div class="rule abs"></div>
    <div class="legal abs">Nexora Tech, LLC.<br>Copyright © 2017</div>
  </div>
  <div class="chat abs">CHAT NOW</div>
</div>
</body>
</html>
```